Keelbrook Vault Holdings Needs A Website

We are looking for a website for a new company. 4 Pages

Needs to be responsive and mobile friendly for all browsers and coded for both Android & IOS. SEO is also important.

Website Brief – Keelbrook Vault Holdings
Domain: www.keelbrookvault.net
Email: info@keelbrookvault.net
Phone: to be inserted later
Address: 40837 52 Ave, Edmonton, AB T6K 3R8
Platform: WordPress (recommended for flexibility, SEO tools, and ease of editing)
Requirements:
• Responsive & mobile-friendly (Android & iOS)
• Cross-browser compatibility
• Fast page load speed
• SEO optimized for storage development, management, and investment keywords
• Easy in-house editing after launch
• Professional, modern, trust-driven design reflecting expertise, reliability, and innovation
________________________________________
Pages
1. HOME
Purpose: Quickly communicate who Keelbrook Vault Holdings is and why they’re the best choice for designing, building, leasing, and managing self storage facilities.
Content Highlights:
• Hero Section: Large, bold image of a modern self storage facility with headline:
"From Concept to Capacity – Your Self Storage Experts"
• Subheadline: “Keelbrook Vault Holdings delivers turnkey design, construction, leasing, and management services for profitable self storage operations.”
• Quick Service Icons:
o Facility Design & Development
o Construction & Build Management
o Lease-Up & Marketing
o Ongoing Facility Management
• Call to Action Button: “LEARN MORE” → links to ABOUT US page.
• Featured Project Highlights: Showcase a few completed or current projects with photos and stats.
• Contact Banner: “Ready to build your next self storage project? Let’s talk.” → CONTACT page.
2. ABOUT US
Purpose: Build credibility, showcase experience, and explain the value proposition.
Content Highlights:
• Who We Are: Overview of Keelbrook Vault Holdings’ history, mission, and team expertise.
• Our Approach: End-to-end process from site selection to occupancy.
• Why Choose Us:
o Industry expertise in self storage
o Proven track record in lease-up success
o Strong vendor and contractor network
3. SERVICES
Purpose: Detail all service offerings with clarity and authority.
Sections:
• Design & Development: Market analysis, site planning, and architectural design.
• Construction Management: Overseeing timelines, budgets, and quality control.
• Lease-Up Strategy: Marketing, promotions, and occupancy acceleration.
• Ongoing Facility Management: Staffing, maintenance, revenue optimization.

4. CONTACT
Purpose: Provide simple, direct ways to connect.
Content Highlights:
• Contact Form (Name, Email, Phone, Message)
• Direct Email: info@keelbrookvault.net
• Phone (if applicable)
• Google Map embed (if there’s a head office location)
• CTA: “Let’s Build Your Storage Success Story.”
Design & Technical Notes
• Visual Style: Clean, modern, bold typography, professional color palette (to be based on branding), strong imagery of self storage facilities.
• Performance: Image compression, caching, responsive scaling.
• SEO Targets: “Self storage facility developer,” “self storage construction,” “self storage management company,” “lease-up services for self storage.”

WordPress or Joomla – must be desktop and mobile friendly with fast page load speed. Need the ability to edit ourselves.

Use pantone colours - #033c5a – dark blue
#2baadf – light blue

```html
<!DOCTYPE html>
<html lang="en">
<head>
<meta charset="utf-8">
<title>Keelbrook Vault Holdings – Self Storage Experts</title>
<link href="https://fonts.googleapis.com/css2?family=Urbanist:wght@300;400;500;600;700;800&family=Inter:wght@400;500;600&display=swap" rel="stylesheet">
<style>
:root{
  --navy:#033c5a;
  --sky:#2baadf;
  --sky-soft:#5cc0ee;
  --ink:#1d2630;
  --muted:#55606b;
  --line:#c9d1d8;
  --backdrop:#e9ecef;
  --white:#ffffff;
}
*{box-sizing:border-box;margin:0;padding:0}
html,body{width:1200px;height:4669px;overflow:hidden}
body{background:var(--backdrop);font-family:"Inter",sans-serif;color:var(--ink);position:relative}
.page{position:absolute;left:51px;top:49px;width:1089px;height:4570px;background:var(--white);overflow:hidden}
.abs{position:absolute}
.h-font{font-family:"Urbanist",sans-serif}
.eyebrow{font-size:12px;font-weight:500;letter-spacing:.3px;text-transform:uppercase;color:var(--ink)}
.heading{font-family:"Urbanist",sans-serif;font-weight:400;font-size:38px;line-height:1.1;color:var(--navy)}
.heading b{font-weight:800}
.btn{position:absolute;display:flex;align-items:center;justify-content:center;border-radius:22px;font-size:13px;font-weight:500}
.btn-navy{background:var(--navy);color:var(--white)}
.btn-white{background:var(--white);color:var(--navy)}
.photo{position:absolute}
.small{font-size:10px;line-height:1.55;color:var(--muted)}

/* hero */
.hero{left:0;top:0;width:1089px;height:607px;background:linear-gradient(105deg,#3aa6e4 0%,#49b3ea 40%,#7cc7ee 62%,#2e4e6a 100%)}
.hero-fade{left:0;top:0;width:1089px;height:607px;background:linear-gradient(90deg,rgba(43,170,223,.85) 0%,rgba(43,170,223,.55) 45%,rgba(3,60,90,0) 75%)}
.nav{left:119px;top:11px;width:851px;height:54px;background:var(--white);border-radius:28px;display:flex;align-items:center;padding:0 6px 0 14px}
.brand{display:flex;align-items:center;gap:8px;font-family:"Urbanist",sans-serif;font-weight:700;font-size:16px;color:var(--navy)}
.brand-mark{width:26px;height:26px;background:var(--navy);border-radius:4px}
.nav-links{display:flex;gap:18px;margin-left:auto;margin-right:auto;font-size:13px;font-weight:500;color:var(--ink);position:relative;left:-20px}
.nav .btn{position:static;width:120px;height:42px}
.hero-title{left:138px;top:166px;font-family:"Urbanist",sans-serif;font-size:54px;line-height:66px;color:var(--white);font-weight:300}
.hero-title b{font-weight:800}
.hero-copy{left:138px;top:373px;width:455px;font-size:12.5px;line-height:1.55;color:var(--white)}
.clients-card{left:759px;top:134px;width:193px;height:145px;background:var(--white);border-radius:8px;padding:12px 14px}
.clients-card .big{font-family:"Urbanist",sans-serif;font-size:34px;font-weight:800;color:var(--sky);display:inline-block;vertical-align:middle}
.clients-card .lbl{display:inline-block;vertical-align:middle;font-family:"Urbanist",sans-serif;font-weight:700;font-size:14px;line-height:1;color:var(--navy)}
.avatars{display:flex;margin-top:10px}
.avatars span{width:34px;height:34px;border-radius:50%;border:2px solid var(--white);margin-right:-6px;background:linear-gradient(135deg,#c9a37f,#6b4a35)}

/* about */
.bullet{display:flex;gap:18px;align-items:flex-start}
.dot{width:8px;height:8px;border-radius:50%;background:var(--sky);margin-top:3px}

/* projects */
.project-title{font-family:"Urbanist",sans-serif;font-size:19px;line-height:1.05;color:var(--ink);display:flex;gap:9px}
.project-title .dot{margin-top:8px;flex:none}
.project-meta{font-size:10px;line-height:1.8;color:var(--ink)}

/* services */
.services{left:0;top:1824px;width:1089px;height:652px;background:var(--navy)}
.svc-title{display:flex;gap:10px;align-items:flex-start;font-family:"Urbanist",sans-serif;font-size:20px;line-height:1.15;color:var(--white)}
.svc-icon{width:42px;height:40px;background:var(--sky);border-radius:3px;flex:none;display:flex;align-items:center;justify-content:center}
.svc-desc{font-size:10px;line-height:1.7;color:#cfe0ea}
.round{position:absolute;width:38px;height:38px;border-radius:50%;display:flex;align-items:center;justify-content:center}

/* benefits */
.stat{position:absolute;left:545px;width:408px;border-bottom:1.5px solid #9aa5ae;height:78px}
.stat .num{font-family:"Urbanist",sans-serif;font-size:32px;font-weight:700;color:var(--ink);line-height:1}
.stat .txt{font-size:10px;color:var(--muted);margin-top:6px}
.stat svg{position:absolute;right:0;top:6px}

/* contact */
.field{position:absolute;border:1px solid var(--line);border-radius:20px;font-size:10px;color:var(--ink);padding:0 16px;display:flex;align-items:center}
.contact-row{position:absolute;left:138px;display:flex;gap:10px;align-items:center}
.contact-row .ic{width:36px;height:36px;border-radius:50%;background:var(--navy);display:flex;align-items:center;justify-content:center}
.contact-row .k{font-size:12px;font-weight:500}
.contact-row .v{font-size:10px;color:var(--muted);margin-top:4px}

/* testimonials */
.face{position:absolute;border-radius:50%;background:linear-gradient(135deg,#9bb5c9,#2c4153);border:3px solid var(--white);box-shadow:0 2px 6px rgba(0,0,0,.15)}
.quote{left:280px;top:3831px;width:529px;text-align:center;font-size:10.5px;line-height:1.75;font-style:italic;color:var(--ink)}

/* footer */
.footer{left:0;top:4103px;width:1089px;height:467px;background:var(--navy);color:var(--white)}
.foot-col{text-align:center;font-size:10.5px;line-height:1.9;color:#dce8ef}
.foot-col h4{font-size:12px;font-weight:500;color:var(--white);margin-bottom:10px}
.social{position:absolute;top:4428px;width:26px;height:26px;border-radius:50%}
</style>
</head>
<body>
<div class="page">

  <!-- HERO -->
  <div class="abs hero"></div>
  <div class="photo" role="img" aria-label="Long row of green roll-up self storage doors under a blue sky" style="left:480px;top:210px;width:609px;height:397px;background:linear-gradient(160deg,rgba(255,255,255,0) 0%,rgba(120,140,150,.35) 45%,rgba(32,60,70,.85) 100%);clip-path:polygon(100% 0,100% 100%,0 100%)"></div>
  <div class="abs hero-fade"></div>

  <nav class="abs nav">
    <div class="brand"><span class="brand-mark"></span>Keelbrook Vault Holdings</div>
    <div class="nav-links"><span>Home</span><span>Company</span><span>Services</span><span>Contact</span></div>
    <span class="btn btn-navy">Get Started</span>
  </nav>

  <h1 class="abs hero-title">From <b>Concept</b> To<br><b>Capacity</b> Your Self<br><b>Storage</b> Experts</h1>
  <p class="abs hero-copy">Keelbrook Vault Holdings Delivers Turnkey Design, Construction, Leasing, And Management Services For Profitable Self Storage Operations</p>
  <span class="btn btn-navy" style="left:138px;top:477px;width:202px;height:40px">Get Your Storage</span>
  <span class="btn btn-white" style="left:351px;top:477px;width:167px;height:40px">Learn More</span>

  <div class="abs clients-card">
    <span class="big">10K+</span> <span class="lbl">Happy<br>Clients</span>
    <p style="font-size:8.5px;line-height:1.5;color:var(--muted);margin-top:4px">Lorem ipsum dolor sit amet consectetur. Est egestas aenean.</p>
    <div class="avatars" role="img" aria-label="Client portrait thumbnails"><span></span><span></span><span></span><span></span><span></span></div>
  </div>

  <!-- ABOUT -->
  <p class="abs eyebrow" style="left:0;width:1089px;top:690px;text-align:center">About Us</p>
  <h2 class="abs heading" style="left:0;width:1089px;top:710px;text-align:center">Where Innovation Meets <b>Reliable</b><br><b>Storage</b> Solutions.</h2>

  <h3 class="abs h-font" style="left:138px;top:832px;font-size:22px;font-weight:500;color:var(--navy)">Who We Are</h3>
  <p class="abs small" style="left:138px;top:873px;width:400px">Lorem Ipsum Dolor Sit Amet Consectetur. Odio Egestas Gravida Est Odio Tellus. Nec Tristique Ac Aliquam Facilisis Facilisi Iaculis Viverra Tellus Nibh. Pellentesque Non Tortor Justo Sapien Magna Ac Mauris Eu Condimentum.</p>
  <p class="abs small" style="left:138px;top:940px;width:400px">Tellus Et Tortor Lectus Sit Faucibus. Ullamcorper Luctus Neque Blandit Maecenas Amet Ut Etiam Proin.</p>
  <div class="abs bullet" style="left:138px;top:1003px">
    <span class="dot"></span><span style="font-size:11px;width:80px">Our Mission</span>
    <span class="small" style="font-size:8.5px;width:180px;margin-top:-1px">Lorem Ipsum Dolor Sit Amet Consectetur. Risus Cursus Cras Volutpat Fringilla In Tincidunt Blandit Nibh Elementum.</span>
  </div>
  <div class="abs bullet" style="left:138px;top:1060px">
    <span class="dot"></span><span style="font-size:11px;width:80px">Our Story</span>
    <span class="small" style="font-size:8.5px;width:180px;margin-top:-1px">Lorem Ipsum Dolor Sit Amet Consectetur. Risus Cursus Cras Volutpat Fringilla In Tincidunt Blandit Nibh Elementum.</span>
  </div>
  <span class="btn btn-navy" style="left:138px;top:1146px;width:183px;height:40px">Discover More</span>

  <div class="abs" style="left:577px;top:838px;width:394px;height:355px;background:var(--navy)"></div>
  <div class="photo" role="img" aria-label="Storage building with blue roll-up doors and an open unit" style="left:567px;top:828px;width:383px;height:354px;background:linear-gradient(120deg,#eef1f4 0%,#c9d2da 40%,#3b78c2 70%,#b7c0c8 100%)"></div>

  <!-- PROJECTS -->
  <p class="abs eyebrow" style="left:138px;top:1278px">Our Projects</p>
  <h2 class="abs heading" style="left:138px;top:1298px">Where <b>Innovation</b> Meets <b>Execution</b></h2>

  <div class="abs" style="left:125px;top:1376px;width:60px;height:60px;background:var(--navy)"></div>
  <div class="photo" role="img" aria-label="Maple Street storage building with blue roof and doors" style="left:138px;top:1387px;width:262px;height:252px;background:linear-gradient(180deg,#6fa8dc 0%,#c7d3de 45%,#8d9298 100%)"></div>
  <div class="photo" role="img" aria-label="Brick self storage building with grey roll-up doors" style="left:413px;top:1387px;width:263px;height:252px;background:linear-gradient(180deg,#c9d5e0 0%,#7a4a3c 40%,#6d6f72 100%)"></div>
  <div class="photo" role="img" aria-label="Single-storey storage row with blue doors under cloudy sky" style="left:691px;top:1387px;width:262px;height:252px;background:linear-gradient(180deg,#8fb7e0 0%,#d8e1ea 45%,#3f6fc2 62%,#6f7378 100%)"></div>

  <div class="abs project-title" style="left:138px;top:1659px"><span class="dot"></span><span>Maple Street Storage –<br>Edmonton, AB</span></div>
  <p class="abs project-meta" style="left:138px;top:1712px">40,000 Sq Ft | 200 Units |<br>Lease-Up Success In 3 Months</p>
  <div class="abs project-title" style="left:413px;top:1659px"><span class="dot"></span><span>Riverbend Self Storage –<br>Calgary, AB</span></div>
  <p class="abs project-meta" style="left:413px;top:1712px">55,000 Sq Ft | 350 Units |<br>Full Management &amp; Maintenance</p>
  <div class="abs project-title" style="left:691px;top:1659px"><span class="dot"></span><span>Downtown Express Storage –<br>Edmonton, AB</span></div>
  <p class="abs project-meta" style="left:691px;top:1712px">30,000 Sq Ft | 180 Units |<br>Construction &amp; Marketing Solutions</p>

  <!-- SERVICES -->
  <section class="abs services">
    <p class="abs eyebrow" style="left:138px;top:47px;color:var(--white)">Services</p>
    <h2 class="abs heading" style="left:138px;top:62px;color:var(--white)">The <b>Services</b> We Offered</h2>
    <span class="btn btn-white" style="left:774px;top:49px;width:183px;height:38px">Discover More</span>

    <div class="photo" role="img" aria-label="Indoor storage corridor with blue unit doors" style="left:138px;top:150px;width:262px;height:289px;background:linear-gradient(180deg,#d6dde4 0%,#a9b6c3 40%,#3d6fbf 75%,#e5ebf0 100%)"></div>
    <div class="photo" role="img" aria-label="Steel frame construction site with workers" style="left:413px;top:150px;width:263px;height:289px;background:linear-gradient(180deg,#9fc3e6 0%,#b9c3cc 45%,#8f7d66 100%)"></div>
    <div class="photo" role="img" aria-label="Open storage unit with boxes inside" style="left:691px;top:150px;width:262px;height:289px;background:linear-gradient(180deg,#c2ccd5 0%,#4b7cc9 45%,#c59d6d 80%,#d9dde1 100%)"></div>
    <div class="photo" role="img" aria-label="Exterior row of storage units" style="left:966px;top:150px;width:140px;height:289px;background:linear-gradient(180deg,#8fb6dd 0%,#c8d2dc 60%,#7b8088 100%)"></div>

    <div class="abs svc-title" style="left:138px;top:452px;width:262px"><span class="svc-icon"><svg width="24" height="24" viewBox="0 0 24 24" fill="none" stroke="#fff" stroke-width="1.6"><rect x="3" y="3" width="18" height="18"/><path d="M3 15l6-6 4 4 5-5"/></svg></span><span>Facility Design &amp;<br>Development</span></div>
    <p class="abs svc-desc" style="left:138px;top:507px;width:262px">Market Analysis, Site Planning, And Architectural Design For Optimized Storage Solutions.</p>

    <div class="abs svc-title" style="left:413px;top:452px;width:263px"><span class="svc-icon"><svg width="24" height="24" viewBox="0 0 24 24" fill="none" stroke="#fff" stroke-width="1.6"><path d="M4 21V9h16v12M8 21v-8h8v8M2 9l10-6 10 6"/></svg></span><span>Construction &amp; Build<br>Management</span></div>
    <p class="abs svc-desc" style="left:413px;top:507px;width:263px">Overseeing Timelines, Budgets, And Quality Control To Bring Your Project To Life.</p>

    <div class="abs svc-title" style="left:691px;top:452px;width:262px"><span class="svc-icon"><svg width="24" height="24" viewBox="0 0 24 24" fill="none" stroke="#fff" stroke-width="1.6"><path d="M3 10v4h4l8 5V5L7 10H3zM18 9a4 4 0 010 6"/></svg></span><span>Lease-Up &amp;<br>Marketing</span></div>
    <p class="abs svc-desc" style="left:691px;top:507px;width:262px">Accelerating Occupancy Through Promotions, Advertising, And Strategic Campaigns.</p>

    <div class="abs svc-title" style="left:966px;top:452px"><span class="svc-icon"><svg width="24" height="24" viewBox="0 0 24 24" fill="none" stroke="#fff" stroke-width="1.6"><circle cx="12" cy="8" r="4"/><path d="M4 21c0-4 4-7 8-7s8 3 8 7"/></svg></span></div>
    <p class="abs svc-desc" style="left:966px;top:507px;width:200px;white-space:nowrap">Staffing, Maintenance, And<br>Smooth Operations.</p>

    <span class="round" style="left:138px;top:619px;background:var(--white)"><svg width="18" height="18" viewBox="0 0 24 24" fill="none" stroke="#033c5a" stroke-width="2"><path d="M20 12H4M10 6l-6 6 6 6"/></svg></span>
    <span class="round" style="left:914px;top:619px;background:var(--sky)"><svg width="18" height="18" viewBox="0 0 24 24" fill="none" stroke="#fff" stroke-width="2"><path d="M4 12h16M14 6l6 6-6 6"/></svg></span>
  </section>

  <!-- BENEFITS -->
  <div class="photo" role="img" aria-label="Aerial view of a modern storage warehouse with a wind turbine and trees" style="left:138px;top:2562px;width:378px;height:527px;border-radius:10px;background:linear-gradient(180deg,#e9eef2 0%,#cdd8df 35%,#9aa7ae 55%,#3f5e3a 80%,#2d4a2b 100%)"></div>
  <p class="abs eyebrow" style="left:545px;top:2566px;font-size:11px">Benefits</p>
  <h2 class="abs heading" style="left:545px;top:2580px;line-height:1.05">Smart <b>Solutions</b> That<br><b>Deliver</b> Measurable<br>Results</h2>

  <div class="stat" style="top:2725px"><div class="num" style="color:var(--sky)">90%</div><div class="txt">Lorem Ipsum Dolor Sit Amet Consectetur. Nulla Nascetur.</div><svg width="22" height="22" viewBox="0 0 24 24" fill="none" stroke="#2baadf" stroke-width="2.2"><path d="M5 19L19 5M8 5h11v11"/></svg></div>
  <div class="stat" style="top:2807px"><div class="num">85%</div><div class="txt">Lorem Ipsum Dolor Sit Amet Consectetur. Suscipit Lobortis Et Nunc.</div><svg width="22" height="22" viewBox="0 0 24 24" fill="none" stroke="#1d2630" stroke-width="2.2"><path d="M5 19L19 5M8 5h11v11"/></svg></div>
  <div class="stat" style="top:2889px"><div class="num">80%</div><div class="txt">Lorem Ipsum Dolor Sit Amet Consectetur. Diam Vel.</div><svg width="22" height="22" viewBox="0 0 24 24" fill="none" stroke="#1d2630" stroke-width="2.2"><path d="M5 19L19 5M8 5h11v11"/></svg></div>
  <div class="stat" style="top:2970px"><div class="num">95%</div><div class="txt">Lorem Ipsum Dolor Sit Amet Consectetur. Diam Vel.</div><svg width="22" height="22" viewBox="0 0 24 24" fill="none" stroke="#1d2630" stroke-width="2.2"><path d="M5 19L19 5M8 5h11v11"/></svg></div>
  <span class="btn btn-navy" style="left:545px;top:3051px;width:202px;height:40px">Get Your Storage</span>

  <!-- CONTACT -->
  <p class="abs eyebrow" style="left:138px;top:3174px">Contact Us</p>
  <h2 class="abs heading" style="left:138px;top:3190px">Get Into Touch</h2>
  <p class="abs small" style="left:138px;top:3246px;width:400px">Lorem Ipsum Dolor Sit Amet Consectetur. Duis Arcu Sed Convallis Scelerisque Accumsan. Tortor Risus Molestie Auctor Faucibus.</p>

  <div class="contact-row" style="top:3316px"><span class="ic"><svg width="16" height="16" viewBox="0 0 24 24" fill="none" stroke="#fff" stroke-width="1.8"><path d="M5 3h4l2 5-3 2a11 11 0 006 6l2-3 5 2v4a2 2 0 01-2 2A17 17 0 013 5a2 2 0 012-2z"/></svg></span><div><div class="k">PHONE:</div><div class="v">+48 XXX XXX XXX</div></div></div>
  <div class="contact-row" style="top:3364px"><span class="ic"><svg width="16" height="16" viewBox="0 0 24 24" fill="none" stroke="#fff" stroke-width="1.8"><rect x="3" y="5" width="18" height="14" rx="1"/><path d="M3 6l9 7 9-7"/></svg></span><div><div class="k">EMAIL:</div><div class="v">info@keelbrookvault.net</div></div></div>
  <div class="contact-row" style="top:3412px"><span class="ic"><svg width="16" height="16" viewBox="0 0 24 24" fill="none" stroke="#fff" stroke-width="1.8"><path d="M12 21s-7-7-7-12a7 7 0 0114 0c0 5-7 12-7 12z"/><circle cx="12" cy="9" r="2.5"/></svg></span><div><div class="k">LOCATION:</div><div class="v">Poland-Wide Service</div></div></div>

  <span class="field" style="left:553px;top:3176px;width:193px;height:37px">Full Name</span>
  <span class="field" style="left:759px;top:3176px;width:194px;height:37px">Email Address</span>
  <span class="field" style="left:553px;top:3227px;width:193px;height:37px">Phone Number</span>
  <span class="field" style="left:759px;top:3227px;width:194px;height:37px">Date</span>
  <span class="field" style="left:553px;top:3278px;width:400px;height:110px;border-radius:10px;align-items:flex-start;padding-top:12px">Special Requests</span>
  <span class="btn btn-navy" style="left:553px;top:3412px;width:400px;height:40px">Request A Quote</span>

  <!-- TESTIMONIALS -->
  <p class="abs eyebrow" style="left:0;width:1089px;top:3537px;text-align:center">Testimonials</p>
  <h2 class="abs heading" style="left:0;width:1089px;top:3555px;text-align:center">What Our <b>Client</b> Say</h2>
  <div class="photo" role="img" aria-label="Faint dotted world map background" style="left:94px;top:3651px;width:906px;height:398px;background:radial-gradient(ellipse at center,rgba(200,210,220,.35) 0%,rgba(255,255,255,0) 70%)"></div>

  <div role="img" aria-label="Client portraits arranged around the featured testimonial">
    <span class="face" style="left:497px;top:3704px;width:90px;height:90px"></span>
    <span class="face" style="left:212px;top:3711px;width:58px;height:58px"></span>
    <span class="face" style="left:358px;top:3731px;width:44px;height:44px"></span>
    <span class="face" style="left:667px;top:3718px;width:44px;height:44px"></span>
    <span class="face" style="left:852px;top:3711px;width:58px;height:58px"></span>
    <span class="face" style="left:146px;top:3840px;width:44px;height:44px"></span>
    <span class="face" style="left:899px;top:3854px;width:44px;height:44px"></span>
    <span class="face" style="left:264px;top:3914px;width:58px;height:58px"></span>
    <span class="face" style="left:754px;top:3914px;width:58px;height:58px"></span>
  </div>
  <span class="round" style="left:568px;top:3766px;width:28px;height:28px;background:#1d7f96;border:2px solid #fff"><svg width="12" height="12" viewBox="0 0 24 24" fill="#fff"><path d="M4 18l3-12h5l-4 12zM13 18l3-12h5l-4 12z"/></svg></span>

  <p class="abs quote">Lorem Ipsum Is Simply Dummy Text Of The Printing And Typesetting Industry. Lorem Ipsum Has Been The Industry's Standard Dummy Text Ever Since The 1500s, When An Unknown Printer Took A Galley Of Type And Scrambled It To Make A Type Specimen Book. It Has Survived Not Only Five Centuries, But Also The Leap Into Electronic Typesetting, Remaining Essentially Unchanged.</p>
  <p class="abs" style="left:0;width:1089px;top:3914px;text-align:center;font-size:12px;font-weight:500">DANA WHITFIELD</p>
  <p class="abs" style="left:0;width:1089px;top:3930px;text-align:center;font-size:9px;font-weight:600">Co - Founder</p>

  <!-- FOOTER -->
  <footer class="abs footer">
    <h2 class="abs heading" style="left:138px;top:78px;color:var(--white)">Get Our Storage Now</h2>
    <span class="btn btn-white" style="left:794px;top:76px;width:158px;height:38px">Get It Now</span>

    <div class="abs foot-col" style="left:100px;top:172px;width:210px">
      <h4>CONTACT US</h4>
      <p>hello@keelbrookvault.net</p>
      <p style="line-height:1.5">Lorem Ipsum Dolor Sit Amet<br>Consectetur.</p>
      <p>(000)-0000-000</p>
    </div>

    <div class="abs" style="left:0;width:1089px;top:198px;display:flex;justify-content:center;align-items:center;gap:10px">
      <span style="width:30px;height:30px;background:var(--white);border-radius:4px"></span>
      <span class="h-font" style="font-size:30px;font-weight:700;color:var(--white)">Keelbrook Vault Holdings</span>
    </div>
    <p class="abs" style="left:394px;width:301px;top:268px;text-align:center;font-size:10px;line-height:1.7;color:#dce8ef">Lorem Ipsum Dolor Sit Amet Consectetur. Leo Ornare Purus Id Ut Sem. Ultricies Risus Vitae Aliquam Sed Tortor.</p>

    <div class="abs foot-col" style="left:860px;top:172px;width:110px">
      <h4>SUPPORT</h4>
      <p>Lorem Ipsum</p><p>Lorem</p><p>Lorem Ipsum</p><p>Lorem Ipsum</p>
    </div>

    <p class="abs" style="left:0;width:1089px;top:462px;text-align:center;font-size:8.5px;color:#dce8ef">© 2025 All Rights Reserved.</p>
  </footer>
  <span class="social" style="left:489px;background:var(--sky)"></span>
  <span class="social" style="left:531px;background:var(--white);opacity:.9"></span>
  <span class="social" style="left:573px;background:#1a5375"></span>
</div>
</body>
</html>
```